Brightway Dwelling & Yard Care - Maintenance & Improvements

Handyman service - Total home improvement and maintenance

We do everything indoors, ie. carpentry, and outdoors, ie. garden maintenance

No job too small or too unusual

7 Days per week
Updates

I want the overall impression not to favour either gender ... eg. maybe don't use the word Handy'man' because we also have a Fixmistress service .... but just stay with a generic theme of home improvement and maintenance

Industry/Entity Type

Home Improvement

Contact Information for Business Card

Brightway Dwelling & Yard Care
7 Days per Week
Total Home Maintenance and Improvements
Handyman | Fixmistress | Our (DIY) Task Pal
Ph: 0487 613 902
www.brightwaydwellingyard.com.au

Requirements
Must have
• The black and white image of various workers, as per attached

```html
<!DOCTYPE html>
<html lang="en">
<head>
<meta charset="utf-8">
<title>Brightway Dwelling &amp; Yard Care – Business Card</title>
<link rel="stylesheet" href="https://fonts.googleapis.com/css2?family=Arimo:wght@400;700&display=swap">
<style>
  :root {
    --page-bg: #ecebe6;
    --green-deep: #1f4a12;
    --green-mid: #3f7f1e;
    --green-bright: #6fb52c;
    --green-glow: #9fd64a;
    --strip-dark: #2c4a22;
    --text-white: #ffffff;
    --text-soft: #e3eed7;
    --accent-lime: #b6f04a;
    --rule: rgba(255,255,255,0.75);
    --photo-warm: #b98c63;
    --photo-red: #8c3d2e;
    --photo-leaf: #4d7a3a;
  }
  * { box-sizing: border-box; margin: 0; padding: 0; }
  html, body {
    width: 1200px; height: 1000px; overflow: hidden;
    background: var(--page-bg);
  }
  .canvas {
    position: relative; width: 1200px; height: 1000px;
    display: flex; flex-direction: column; align-items: center;
    justify-content: center; gap: 48px;
  }
  .card {
    position: relative; width: 780px; height: 430px;
    border-radius: 30px; overflow: hidden;
    background:
      radial-gradient(ellipse 70% 90% at 30% 20%, var(--green-glow) 0%, transparent 60%),
      linear-gradient(160deg, var(--green-bright) 0%, var(--green-mid) 45%, var(--green-deep) 100%);
    box-shadow: 0 10px 24px rgba(0,0,0,0.18);
  }
  .card__swoosh {
    position: absolute; inset: 0; width: 100%; height: 100%;
  }
  .brand-name {
    position: absolute;
    font-family: "Arimo", sans-serif; font-weight: 700;
    font-size: 38px; line-height: 1.12;
    color: var(--text-white);
    white-space: nowrap;
  }
  .brand-name span { display: block; }

  /* front */
  .card--front .brand-name { left: 52px; bottom: 56px; }
  .front-photo {
    position: absolute; top: 0; right: 0; width: 300px; height: 100%;
    clip-path: polygon(60px 0, 100% 0, 100% 100%, 0 100%);
    background: linear-gradient(180deg, #5e5d5a 0%, var(--photo-red) 35%, var(--photo-warm) 62%, var(--photo-leaf) 100%);
  }

  /* back */
  .card--back .brand-name { left: 48px; top: 44px; }
  .back-rule {
    position: absolute; left: 48px; top: 150px; width: 560px;
    height: 2px; background: var(--rule);
  }
  .back-details {
    position: absolute; left: 48px; top: 172px; width: 570px;
    font-family: "Arimo", sans-serif; color: var(--text-soft);
    font-size: 15px; line-height: 1.7; white-space: nowrap;
  }
  .back-details .contact {
    margin-top: 8px; color: var(--accent-lime); font-weight: 700;
  }
  .back-bottom-rule {
    position: absolute; left: 48px; bottom: 60px; width: 560px;
    height: 2px; background: var(--rule);
  }
  .worker-strip {
    position: absolute; top: 0; right: 0; width: 130px; height: 100%;
    background: linear-gradient(90deg, var(--strip-dark), #1c3516);
    border-left: 3px solid var(--green-glow);
  }
</style>
</head>
<body>
<main class="canvas">

  <section class="card card--front" aria-label="Business card front">
    <svg class="card__swoosh" viewBox="0 0 780 430" preserveAspectRatio="none" aria-hidden="true">
      <path d="M0 250 C200 200 380 120 520 0 L560 0 C420 150 220 250 0 300 Z" fill="rgba(255,255,255,0.12)"/>
      <path d="M0 330 C220 280 400 200 500 80 L520 90 C420 220 230 310 0 360 Z" fill="rgba(0,0,0,0.10)"/>
    </svg>
    <div class="front-photo" role="img" aria-label="Photo collage of home improvement work: a person working on timber framing, a verandah with wooden railings and garden greenery"></div>
    <h1 class="brand-name"><span>Brightway Dwelling</span><span>&amp; Yard Care</span></h1>
  </section>

  <section class="card card--back" aria-label="Business card back">
    <svg class="card__swoosh" viewBox="0 0 780 430" preserveAspectRatio="none" aria-hidden="true">
      <path d="M0 90 C200 60 420 40 650 0 L680 0 C440 60 220 90 0 130 Z" fill="rgba(255,255,255,0.12)"/>
    </svg>
    <h2 class="brand-name"><span>Brightway Dwelling</span><span>&amp; Yard Care</span></h2>
    <div class="back-rule"></div>
    <div class="back-details">
      <p>7 Days per Week &nbsp;|&nbsp; Total Home Maintenance and Improvements Handyman</p>
      <p>Fixmistress &nbsp;|&nbsp; Our (DIY) Task Pal</p>
      <p class="contact">Ph: 0487 613 902 &nbsp;|&nbsp; www.brightwaydwellingyard.com.au</p>
    </div>
    <div class="back-bottom-rule"></div>
    <div class="worker-strip" role="img" aria-label="Column of white pictograms of workers doing household and garden tasks: painting, sawing, mowing, carrying, cleaning"></div>
  </section>

</main>
</body>
</html>
```